A Book Cover For a Book Called "Lantern"

Attached are two files for the ISBN bar graph for the print version of the cover! Same image, just two different formats.
Updates

Target Market(s)

young adult female, parents

Colors

```html
<!DOCTYPE html>
<html lang="en">
<head>
<meta charset="utf-8">
<title>Lantern — A Memoir</title>
<link rel="stylesheet" href="https://fonts.googleapis.com/css2?family=Yellowtail&family=Cinzel:wght@400&family=Handlee&display=swap">
<style>
  :root {
    --page-bg: #5b5659;
    --cover-black: #050305;
    --ink-white: #f4f2f3;
    --ink-soft: #d9d4d8;
    --shoe-pink: #e6c7c9;
    --shoe-shadow: #7a4d63;
    --brick-orange: #c46a35;
    --haze-violet: #3a2233;
  }
  * { margin: 0; padding: 0; box-sizing: border-box; }
  html, body {
    width: 1200px;
    height: 1200px;
    overflow: hidden;
    background: var(--page-bg);
  }
  .stage {
    width: 1200px;
    height: 1200px;
    display: flex;
    align-items: center;
    justify-content: center;
  }
  .book-cover {
    position: relative;
    width: 754px;
    height: 1160px;
    background: var(--cover-black);
    overflow: hidden;
  }
  .cover-title {
    position: absolute;
    top: 78px;
    left: 0;
    width: 100%;
    text-align: center;
    color: var(--ink-white);
  }
  .cover-title__main {
    display: block;
    font-family: "Yellowtail", cursive;
    font-size: 104px;
    line-height: 1;
    font-weight: 400;
    margin-left: 40px;
  }
  .cover-title__sub {
    display: block;
    font-family: "Cinzel", serif;
    font-size: 28px;
    letter-spacing: 4px;
    color: var(--ink-soft);
    margin-top: -10px;
    margin-left: 110px;
  }
  .cover-photo {
    position: absolute;
    left: 110px;
    top: 210px;
    width: 560px;
    height: 860px;
    background:
      radial-gradient(ellipse 22% 30% at 54% 52%, var(--shoe-pink) 0%, rgba(230,199,201,0.55) 45%, transparent 75%),
      radial-gradient(ellipse 30% 8% at 60% 82%, var(--brick-orange) 0%, rgba(196,106,53,0.5) 50%, transparent 85%),
      radial-gradient(ellipse 25% 25% at 30% 50%, var(--shoe-shadow) 0%, transparent 80%),
      radial-gradient(ellipse 55% 50% at 50% 55%, var(--haze-violet) 0%, transparent 85%);
  }
  .cover-author {
    position: absolute;
    bottom: 42px;
    left: 0;
    width: 100%;
    text-align: center;
    font-family: "Handlee", cursive;
    font-size: 27px;
    color: var(--ink-soft);
    letter-spacing: 0.5px;
  }
</style>
</head>
<body>
  <main class="stage">
    <article class="book-cover">
      <h1 class="cover-title">
        <span class="cover-title__main">Lantern</span>
        <span class="cover-title__sub">A Memoir</span>
      </h1>
      <div class="cover-photo" role="img" aria-label="Photograph of a dancer's foot en pointe in a pink satin ballet shoe, balanced on a weathered brick against a dark, textured background"></div>
      <p class="cover-author">by Willow Hart with Maren Cole</p>
    </article>
  </main>
</body>
</html>
```